Stylish Business Card for Modern hair salon

I need a simple business card design using our salon logo and colours that are in the logo. We service clients of all ages but predominantly those in the 18 to 55 age range. We have a young staff and are looking to have a card that will present a modern and clean image that represents who we are. The card should be in black and white same as our logo. Minimal use of other colours is allowed.

Industry/Entity Type

Hair And Beauty

Contact Information for Business Card

The design should have the following information
salon name - TR Hair Studio
address - 2751 Birchfield Rd.E. Mississauga, ON L7P3K2
phone - 905 614-2870
website - trhairexample.ca
instagram - tr.hairstudio
twitter - @TR_HairStudio

Colors
000000
ffffff
474747

Requirements
Must have
• simple design, salon name, address, phone, website, instagram, twitter info
• Back of card should have the following:
• YOUR NEXT APPOINTMENT
• DATE
• TIME
Nice to have
• simple design, clear to see and read,
• predominantly black and white colour, minimal use of other colours is ok
Should not have
• many colours, various fonts

```html
<!DOCTYPE html>
<html lang="en">
<head>
<meta charset="utf-8">
<title>TR Hair Studio – Business Card</title>
<link rel="stylesheet" href="https://fonts.googleapis.com/css2?family=Tinos&display=swap">
<style>
  :root {
    --ink: #000000;
    --paper: #ffffff;
    --text-dark: #2b2b2b;
    --grey: #a7a9ac;
    --card-edge: #474747;
  }
  * { margin: 0; padding: 0; box-sizing: border-box; }
  html, body {
    width: 1116px;
    height: 1200px;
    overflow: hidden;
    background: var(--paper);
  }
  body {
    position: relative;
    font-family: "Tinos", "Times New Roman", serif;
  }
  .card {
    position: absolute;
    left: 82px;
    width: 957px;
    height: 547px;
    background: var(--ink);
    border: 1px solid var(--card-edge);
    color: var(--paper);
  }
  .card--front { top: 24px; }
  .card--back { top: 623px; left: 83px; }

  .brand-name {
    position: absolute;
    left: 42px;
    top: 36px;
    font-size: 90px;
    line-height: 1;
    font-weight: 400;
    color: var(--paper);
  }
  .brand-rule {
    position: absolute;
    left: 43px;
    top: 158px;
    width: 878px;
    height: 2px;
    background: var(--paper);
  }
  .studio-title {
    position: absolute;
    left: 0;
    width: 100%;
    top: 194px;
    padding-left: 20px;
    text-align: center;
    font-size: 46px;
    font-weight: 400;
    letter-spacing: 0.5px;
  }
  .contact-list {
    position: absolute;
    left: 55px;
    top: 276px;
    list-style: none;
    font-size: 30px;
    line-height: 42.3px;
  }

  .appointment-art { position: absolute; inset: 0; }
  .appointment-heading {
    font-size: 38px;
    fill: var(--text-dark);
  }
  .appointment-label {
    font-size: 48px;
    fill: var(--text-dark);
  }
  .appointment-art text { font-family: "Tinos", "Times New Roman", serif; }
</style>
</head>
<body>

<section class="card card--front">
  <div class="brand-name">TR Hair</div>
  <div class="brand-rule"></div>
  <h1 class="studio-title">TR Hair Studio</h1>
  <ul class="contact-list">
    <li>Address - 2751 Birchfield Rd.E. Mississauga, ON L7P3K2</li>
    <li>Phone - 905 614-2870</li>
    <li>Website - trhairexample.ca</li>
    <li>Instagram - tr.hairstudio</li>
    <li>Twitter - @TR_HairStudio</li>
  </ul>
</section>

<section class="card card--back">
  <svg class="appointment-art" width="957" height="547" viewBox="0 0 957 547">
    <rect class="frame-grey" x="49" y="47" width="831" height="480" rx="48" fill="none" stroke="var(--grey)" stroke-width="3"/>
    <rect class="frame-white" x="76" y="31" width="829" height="480" rx="48" fill="none" stroke="var(--paper)" stroke-width="3"/>
    <rect class="panel-shadow" x="92" y="95" width="742" height="392" rx="56" fill="var(--grey)"/>
    <rect class="panel" x="113" y="73" width="749" height="390" rx="56" fill="var(--paper)"/>
    <text class="appointment-heading" x="494" y="135" text-anchor="middle">YOUR NEXT APPOINTMENT</text>
    <line class="heading-rule" x1="219" y1="147" x2="771" y2="147" stroke="var(--text-dark)" stroke-width="1.5"/>
    <text class="appointment-label" x="180" y="230">Date</text>
    <text class="appointment-label" x="338" y="230">:</text>
    <text class="appointment-label" x="180" y="291">Time</text>
    <text class="appointment-label" x="338" y="291">:</text>
  </svg>
</section>

</body>
</html>
```